BRISK Study flyer

I need help designing a flyer for a research study that will include brain imaging in adolescents. The info is in the attached document. The study is called the Brain Rhythms In School Kids (BRISK) study. Ideally this would be returned as a document that I can edit in the future as we will have several new recruitment phases (different age groups, etc. I also would love to have a logo designed as part of this project, but I recognize that might be a separate design request.

```html
<!DOCTYPE html>
<html lang="en">
<head>
<meta charset="utf-8">
<title>BRISK Study Recruitment Flyer</title>
<link href="https://fonts.googleapis.com/css2?family=Lato:wght@400;700;900&display=swap" rel="stylesheet">
<style>
  :root {
    --navy: #13358c;
    --navy-light: #274b9b;
    --gold: #fdb71f;
    --gold-soft: #fde3a6;
    --ink: #141414;
    --mist: #efeff2;
    --white: #ffffff;
  }
  * { box-sizing: border-box; margin: 0; padding: 0; }
  html, body { width: 927px; height: 1200px; overflow: hidden; background: var(--white); }
  body { font-family: "Lato", sans-serif; color: var(--ink); }
  .flyer { position: relative; width: 927px; height: 1200px; overflow: hidden; background: var(--white); }

  .hero-photo {
    position: absolute; left: 0; top: 0; width: 927px; height: 310px;
    background: linear-gradient(100deg, #b9bcb4 0%, #8e8b83 35%, #6f6a63 55%, #b8a594 70%, #6d8fae 85%, #4a4036 100%);
  }
  .gold-band { position: absolute; left: 0; top: 309px; width: 927px; height: 124px; background: var(--gold); }

  .intro-panel { position: absolute; left: 60px; top: 140px; width: 359px; height: 445px; }
  .intro-panel__top { position: absolute; left: 0; top: 0; width: 359px; height: 171px; background: var(--navy); }
  .intro-panel__bottom {
    position: absolute; left: 0; top: 170px; width: 359px; height: 275px;
    background: var(--navy-light); border-bottom-right-radius: 160px;
  }
  .brand { position: absolute; left: 45px; top: 68px; display: flex; align-items: center; gap: 10px; }
  .brand__mark { width: 14px; height: 14px; background: var(--gold); }
  .brand__name { color: var(--white); font-weight: 700; font-size: 25px; line-height: 1; }
  .intro-panel__question {
    position: absolute; left: 45px; top: 243px; color: var(--white);
    font-weight: 700; font-size: 33px; line-height: 40px;
  }

  .hook {
    position: absolute; left: 466px; top: 338px; color: var(--navy);
    font-weight: 700; font-size: 31px; line-height: 37px;
  }
  .summary { position: absolute; left: 466px; top: 462px; width: 400px; font-size: 20px; line-height: 25.5px; }
  strong { font-weight: 700; }

  .section-title { position: absolute; left: 60px; color: var(--navy); font-weight: 700; font-size: 23px; line-height: 1; }
  .section-title--involves { top: 623px; }
  .section-title--eligible { top: 974px; }

  .task-icon { position: absolute; background: var(--gold-soft); border-radius: 12px; }
  .task-icon--interview { left: 65px; top: 677px; width: 74px; height: 75px; }
  .task-icon--survey { left: 464px; top: 684px; width: 83px; height: 62px; }
  .task-icon--visit { left: 67px; top: 794px; width: 69px; height: 69px; }
  .task-text { position: absolute; font-size: 19px; line-height: 23.6px; }
  .task-text--interview { left: 160px; top: 678px; width: 285px; }
  .task-text--survey { left: 562px; top: 678px; width: 260px; }
  .task-text--visit { left: 160px; top: 791px; width: 650px; }

  .eligibility-area { position: absolute; left: 0; top: 941px; width: 927px; height: 259px; background: var(--mist); }
  .criteria { position: absolute; left: 60px; top: 1024px; width: 459px; list-style: none; }
  .criteria__item { position: relative; padding-left: 31px; font-size: 19px; line-height: 23.6px; }
  .criteria__item + .criteria__item { border-top: 1px solid var(--navy); }
  .criteria__item:nth-child(1) { height: 34px; }
  .criteria__item:nth-child(2) { height: 39px; padding-top: 7px; }
  .criteria__item:nth-child(3) { padding-top: 10px; }
  .criteria__arrow { position: absolute; left: 0; width: 13px; height: 13px; }
  .criteria__item:nth-child(1) .criteria__arrow { top: 6px; }
  .criteria__item:nth-child(2) .criteria__arrow { top: 13px; }
  .criteria__item:nth-child(3) .criteria__arrow { top: 16px; }

  .contact-card {
    position: absolute; left: 522px; top: 902px; width: 338px; height: 298px;
    background: var(--gold); border-top-left-radius: 74px;
  }
  .contact-card__prompt {
    position: absolute; left: 30px; top: 77px; color: var(--navy);
    font-size: 20px; line-height: 25px;
  }
  .contact-card__prompt strong { font-weight: 700; }
  .contact-email {
    position: absolute; left: 552px; top: 1081px; width: 320px; height: 50px;
    background: var(--navy); color: var(--white); font-weight: 700; font-size: 22px;
    line-height: 50px; padding-left: 20px;
  }
</style>
</head>
<body>
<main class="flyer">
  <div class="hero-photo" role="img" aria-label="Photo of a thoughtful teenage girl with a braid, in a blue t-shirt, gazing to the side in a living room"></div>
  <div class="gold-band"></div>

  <section class="intro-panel">
    <div class="intro-panel__top">
      <div class="brand">
        <span class="brand__mark"></span>
        <span class="brand__name">Northvale University</span>
      </div>
    </div>
    <div class="intro-panel__bottom"></div>
    <h1 class="intro-panel__question">Are you the<br>parent of a child<br>age 10-17?</h1>
  </section>

  <h2 class="hook">Do they worry or overthink<br>negative emotions?</h2>

  <p class="summary">Northvale University researchers are <strong>seeking girls age 10-17</strong> for a <strong>study about brain activity in emotions and decision-making</strong> and how they relate to <strong>puberty, anxiety and depression.</strong></p>

  <h3 class="section-title section-title--involves">Study participation involves:</h3>

  <div class="task-icon task-icon--interview" role="img" aria-label="Line icon of a smiling head with a tangle of thoughts"></div>
  <p class="task-text task-text--interview">One one-hour interview (online or in-person) where your <strong>child</strong> will discuss <strong>their thoughts</strong></p>

  <div class="task-icon task-icon--survey" role="img" aria-label="Line icon of two leaves around a small figure"></div>
  <p class="task-text task-text--survey">Online questionnaires<br><strong>(parent and child)</strong></p>

  <div class="task-icon task-icon--visit" role="img" aria-label="Line icon of two overlapping theatre masks"></div>
  <p class="task-text task-text--visit">One two-hour visit where your child will complete an <strong>MRI scan, answer questions</strong> about their puberty stage, and have a small <strong>hair sample</strong> taken to study <strong>puberty hormones</strong></p>

  <div class="eligibility-area"></div>
  <h3 class="section-title section-title--eligible">Your child may be eligible if they:</h3>
  <ul class="criteria">
    <li class="criteria__item">
      <svg class="criteria__arrow" viewBox="0 0 13 13"><path d="M0 0 L13 6.5 L0 13 L4 6.5 Z" fill="var(--navy)"/></svg>
      Are <strong>age 10-17</strong>
    </li>
    <li class="criteria__item">
      <svg class="criteria__arrow" viewBox="0 0 13 13"><path d="M0 0 L13 6.5 L0 13 L4 6.5 Z" fill="var(--navy)"/></svg>
      Tend to <strong>worry or overthink negative thoughts</strong>
    </li>
    <li class="criteria__item">
      <svg class="criteria__arrow" viewBox="0 0 13 13"><path d="M0 0 L13 6.5 L0 13 L4 6.5 Z" fill="var(--navy)"/></svg>
      Have <strong>not</strong> been diagnosed with <strong>psychosis,<br>learning problems, or autism</strong>
    </li>
  </ul>

  <aside class="contact-card">
    <p class="contact-card__prompt">Interested in participating?<br>Want more information?<br><strong>Please contact us!</strong></p>
  </aside>
  <div class="contact-email">briskstudy@northvale.edu</div>
</main>
</body>
</html>
```